Business Card Design for Vintage Jazz

I am a vintage jazz band leader in New York City. My groups play the music of the 1920s, 1930s and 1940s. My website is marlowpeskin.com for more info on what I do.

I am looking for a two sided business card design that has the look and feel of a really nice business card from the 1930s. I need to convey with the design that my work has that vintage kind of class and style, but also conveys that we are fun and entertaining.

Most importantly it should make a bold staement. If Hollis Varnum had a card, what would it have looked like? I want a card that I feel confident will make an impact and will let people know that my work is te the top that NYC has to offer in vintage jazz..

Note that I have only decided to avoid the "committed payment" option as I have not used this service before. Assuming that I get quality work I will select a design from those presented.

Target Market(s)

people who want to hire my band for events, media, and new fans of the band

Industry/Entity Type

Performing Art

Contact Information for Business Card

Definitely a matte finish, possibly a sort of old style of paper with that brown tint? definitely a thick card.

Requirements
Must have
• FRONT
• My name: Marlow Peskin
• What I do: Bandleader, Guitarist, Vocalist, Songwriter
• Contact Details: marlowpeskin.com marlow@marlowpeskin.com 646-555-0187
• BACK
• My Social Media Links:
• facebook.marlowpeskin.com
• twitter, instagram, linkedin: marlowpeskin
• I'm also including a photo image I would like to use. The photo's background is not needed, and to be honest isn't really desireable. Just looking to use the image of me.
Nice to have
• I'm attaching which could be used as is, omitted from the card, or altered maybe with text going around the outside of the circle or in some other way. It may need some clean up to the edges of the lettering as we only use it for the website thumbnail.
• If there's space I'd like to include the text "join our mailing list for a free song download: freesong.marlowpeskin.com" If not perhaps just "Download a Free Song at: freesong.marlowpeskin.com - something to this end.
Should not have
• anything cartoony. Don't think retro 90s's vision of the swing era, think actual swing era!
• anything modern. Got to look old school
• Try to avoid dark backgrounds. Since we often play in bars and clubs where it is dar, a d
• avoid script fonts.

```html
<!DOCTYPE html>
<html lang="en">
<head>
<meta charset="utf-8">
<title>Marlow Peskin — Business Card</title>
<link href="https://fonts.googleapis.com/css2?family=Jost:wght@300;400;600;700&display=swap" rel="stylesheet">
<style>
  :root {
    --page: #d9d9d9;
    --ink: #1f1f1f;
    --ink-soft: #2c2c2c;
    --grey-dark: #6e6e6e;
    --grey-mid: #a8a8a8;
    --grey-light: #f4f4f4;
    --teal-dark: #6e9a96;
    --teal-mid: #b9dad6;
    --teal-light: #eef9f7;
    --white: #ffffff;
  }
  * { box-sizing: border-box; margin: 0; padding: 0; }
  html, body { width: 1200px; height: 1200px; overflow: hidden; }
  body {
    background: var(--page);
    font-family: "Jost", "Futura", sans-serif;
    color: var(--ink);
    display: flex;
    flex-direction: column;
    align-items: center;
    justify-content: center;
    gap: 60px;
  }
  .card {
    position: relative;
    width: 880px;
    height: 472px;
    overflow: hidden;
    box-shadow: 0 6px 18px rgba(0,0,0,0.28);
  }

  /* FRONT */
  .card-front {
    background:
      radial-gradient(ellipse at 42% 78%, var(--grey-light) 0%, #d4d4d4 38%, var(--grey-mid) 70%, var(--grey-dark) 100%);
  }
  .portrait {
    position: absolute;
    left: 0; top: 0;
    width: 460px; height: 472px;
    background: linear-gradient(160deg, #5a5a5a 0%, #2a2a2a 45%, #8a8a8a 80%, #cfcfcf 100%);
  }
  .name {
    position: absolute;
    right: 28px; top: 28px;
    font-weight: 700;
    font-size: 46px;
    letter-spacing: 2px;
    text-transform: uppercase;
    color: var(--white);
    text-align: right;
    text-shadow: 2px 3px 4px rgba(0,0,0,0.55);
    line-height: 1.1;
    white-space: nowrap;
  }
  .roles {
    position: absolute;
    left: 515px; top: 106px;
    list-style: none;
    font-weight: 300;
    font-size: 33px;
    line-height: 42px;
    color: var(--ink-soft);
  }
  .contact {
    position: absolute;
    right: 28px; top: 304px;
    text-align: right;
    font-style: normal;
    font-weight: 300;
    font-size: 27px;
    line-height: 34px;
    color: var(--ink);
  }

  /* BACK */
  .card-back {
    background: radial-gradient(ellipse at 72% 62%, var(--teal-light) 0%, var(--teal-mid) 55%, var(--teal-dark) 100%);
  }
  .mailing {
    position: absolute;
    left: 150px; top: 44px;
    width: 310px;
    text-align: center;
  }
  .mailing-title {
    font-weight: 700;
    font-size: 27px;
    line-height: 1.2;
    white-space: nowrap;
  }
  .mailing-url {
    font-weight: 400;
    font-size: 25px;
    margin-top: 2px;
    white-space: nowrap;
  }
  .brand-mark {
    position: absolute;
    right: 50px; top: 24px;
    width: 248px; height: 248px;
    border-radius: 50%;
    background: var(--white);
    box-shadow: 4px 6px 10px rgba(0,0,0,0.35);
    display: flex;
    align-items: center;
    justify-content: center;
    text-align: center;
    font-weight: 600;
    font-size: 32px;
    line-height: 1.1;
    color: var(--ink);
  }
  .socials {
    position: absolute;
    left: 102px; top: 290px;
    list-style: none;
  }
  .socials li {
    display: flex;
    align-items: center;
    gap: 36px;
    height: 40px;
    font-size: 26px;
    font-weight: 400;
    white-space: nowrap;
  }
  .social-chip {
    width: 32px; height: 32px;
    background: var(--grey-dark);
    flex: none;
  }
</style>
</head>
<body>

  <section class="card card-front" aria-label="Business card front">
    <div class="portrait" role="img" aria-label="Black and white photo of the bandleader in a striped-lapel blazer tipping a straw boater hat"></div>
    <h1 class="name">Marlow Peskin</h1>
    <ul class="roles">
      <li>Bandleader</li>
      <li>Guitarist</li>
      <li>Vocalist</li>
      <li>Songwriter</li>
    </ul>
    <address class="contact">
      646-555-0187<br>
      marlow@marlowpeskin.com<br>
      marlowpeskin.com
    </address>
  </section>

  <section class="card card-back" aria-label="Business card back">
    <div class="mailing">
      <p class="mailing-title">Join our mailing list<br>for a free song download:</p>
      <p class="mailing-url">freesong.marlowpeskin.com</p>
    </div>
    <div class="brand-mark">Marlow<br>Peskin</div>
    <ul class="socials">
      <li><span class="social-chip"></span>connect.marlowpeskin.com/rhythm-club</li>
      <li><span class="social-chip"></span>social.marlowpeskin.com/music</li>
      <li><span class="social-chip"></span>photos.marlowpeskin.com/</li>
      <li><span class="social-chip"></span>posts.marlowpeskin.com</li>
    </ul>
  </section>

</body>
</html>
```